Luminously Grounded Vitality

We want to design a business card that is modern and appealing for an innovative psychedelic telemedicine company that provides at-home ketamine-assisted therapy along with wellness, longevity, and anti-aging medicines. We want to use our deep purple and white plus other colors you can find on our website. We don't have any strict brand guidelines yet so feel free to get creative. We want a very professional, but technology first modern design that will instill trust, peace, calm, but also be attractive to investors in the healthcare and SaaS space.

```html
<!DOCTYPE html>
<html lang="en">
<head>
<meta charset="utf-8">
<title>Luminously Grounded Vitality – Business Card</title>
<link href="https://fonts.googleapis.com/css2?family=Ubuntu:wght@400;500;700&display=swap" rel="stylesheet">
<style>
  :root {
    --bg: #e4e5e8;
    --white: #ffffff;
    --violet: #7b67a9;
    --mauve: #b070a2;
    --mauve-soft: #bd82b0;
    --ink: #2b2b33;
  }
  * { margin: 0; padding: 0; box-sizing: border-box; }
  html, body { width: 1200px; height: 803px; overflow: hidden; }
  body {
    background: var(--bg);
    font-family: "Ubuntu", sans-serif;
    color: var(--ink);
  }
  .canvas {
    position: relative;
    width: 1200px;
    height: 803px;
  }
  .card {
    position: absolute;
    top: 250px;
    width: 520px;
    height: 300px;
    overflow: hidden;
    box-shadow: 0 12px 28px rgba(0,0,0,0.16);
  }
  .card--front { left: 50px; background: var(--white); }
  .card--back { left: 630px; background: var(--mauve); }

  .front-bands { position: absolute; inset: 0; }

  .brand {
    position: absolute;
    display: flex;
    align-items: center;
    gap: 10px;
  }
  .brand__dot {
    width: 14px; height: 14px; border-radius: 50%;
    flex: none;
  }
  .brand__name {
    font-weight: 400;
    line-height: 1.2;
  }
  .card--front .brand { left: 44px; top: 188px; }
  .card--front .brand__dot { background: var(--mauve); }
  .card--front .brand__name { color: var(--mauve); font-size: 17px; }

  .contact {
    position: absolute;
    left: 262px;
    top: 92px;
    font-size: 11.5px;
    line-height: 1.45;
  }
  .contact__name {
    color: var(--violet);
    font-weight: 700;
    font-size: 17px;
    line-height: 1.2;
  }
  .contact__role { font-size: 14px; margin-bottom: 12px; }
  .contact__address { margin-bottom: 10px; }
  .contact__list { list-style: none; }
  .contact__list li { display: flex; align-items: center; gap: 7px; }
  .contact__icon {
    width: 13px; height: 13px; border-radius: 50%;
    background: var(--mauve);
    display: flex; align-items: center; justify-content: center;
    flex: none;
  }

  .back-map {
    position: absolute;
    left: 90px; top: 20px;
    width: 380px; height: 250px;
    border-radius: 40% 50% 45% 40%;
    background: radial-gradient(ellipse at center, var(--mauve-soft) 0%, rgba(176,112,162,0) 70%);
  }
  .card--back .brand {
    left: 0; right: 0; top: 118px;
    justify-content: center;
  }
  .card--back .brand__dot { background: var(--white); }
  .card--back .brand__name { color: var(--white); font-size: 22px; }
  .back-url {
    position: absolute;
    left: 0; right: 0; top: 172px;
    text-align: center;
    color: var(--white);
    font-size: 12px;
    letter-spacing: 4px;
  }
</style>
</head>
<body>
<main class="canvas">

  <section class="card card--front" aria-label="Business card front">
    <svg class="front-bands" viewBox="0 0 520 300" width="520" height="300" aria-hidden="true">
      <polygon points="0,0 520,0 520,4 0,62" fill="var(--violet)"/>
      <polygon points="0,78 520,10 520,18 0,90" fill="var(--violet)"/>
      <polygon points="520,250 520,300 290,300" fill="var(--mauve)"/>
    </svg>

    <div class="brand">
      <span class="brand__dot"></span>
      <span class="brand__name">Luminously Grounded<br>Vitality</span>
    </div>

    <div class="contact">
      <p class="contact__name">Mara Ellison, FNP-C</p>
      <p class="contact__role">Co-founder</p>
      <p class="contact__address">2480 Larkspur Avenue, Suite 300,<br>Fairview, CO, United States</p>
      <ul class="contact__list">
        <li>
          <span class="contact__icon">
            <svg width="8" height="8" viewBox="0 0 10 10" aria-hidden="true"><path d="M2 1h2l1 2.5-1.2 1a5 5 0 0 0 2.7 2.7l1-1.2L10 7v2a1 1 0 0 1-1 1A8 8 0 0 1 1 2a1 1 0 0 1 1-1z" fill="#fff"/></svg>
          </span>+1 555-014-2290
        </li>
        <li>
          <span class="contact__icon">
            <svg width="8" height="8" viewBox="0 0 10 10" aria-hidden="true"><rect x="1" y="2.5" width="8" height="5.5" fill="none" stroke="#fff" stroke-width="1"/><path d="M1 2.5l4 3 4-3" fill="none" stroke="#fff" stroke-width="1"/></svg>
          </span>hello@luminouslyvitality.com
        </li>
        <li>
          <span class="contact__icon">
            <svg width="9" height="9" viewBox="0 0 10 10" aria-hidden="true"><circle cx="5" cy="5" r="3.8" fill="none" stroke="#fff" stroke-width="0.9"/><ellipse cx="5" cy="5" rx="1.6" ry="3.8" fill="none" stroke="#fff" stroke-width="0.8"/><path d="M1.2 5h7.6" stroke="#fff" stroke-width="0.8"/></svg>
          </span>www.luminouslyvitality.com
        </li>
      </ul>
    </div>
  </section>

  <section class="card card--back" aria-label="Business card back">
    <div class="back-map" role="img" aria-label="Faint dotted world map in a lighter mauve tone"></div>
    <div class="brand">
      <span class="brand__dot"></span>
      <span class="brand__name">Luminously Grounded Vitality</span>
    </div>
    <p class="back-url">www.luminouslyvitality.com</p>
  </section>

</main>
</body>
</html>
```